Brochure for Home Improvement Startup

We need an eye-catching, informative, and easy to read brochure design to help explain our services to our target audience which include baby boomers and seniors.

Baby

```html
<!DOCTYPE html>
<html lang="en">
<head>
<meta charset="utf-8">
<title>NestWell Brochure</title>
<link href="https://fonts.googleapis.com/css2?family=Open+Sans:ital,wght@0,400;0,600;0,700;1,400&display=swap" rel="stylesheet">
<style>
:root{
  --stage:#8f8f8f;
  --magenta:#c2185b;
  --magenta-soft:#e04b8e;
  --charcoal:#58585a;
  --ink:#222;
  --heading-grey:#4a4a4c;
  --blue:#2a6db3;
  --blue-soft:#c7dcf1;
  --blue-bar:#7fb1e6;
  --pink-bar:#f05a9f;
  --grey-bar:#5a5a5c;
  --paper:#ffffff;
}
*{margin:0;padding:0;box-sizing:border-box}
html,body{width:800px;height:1200px;overflow:hidden}
body{background:var(--stage);font-family:"Open Sans",Arial,sans-serif;color:var(--ink);position:relative}

.sheet{position:absolute;left:66px;width:668px;overflow:hidden;background:var(--paper)}
.sheet--outside{top:62px;height:518px}
.sheet--inside{top:618px;height:516px}

/* outside */
.room-photo{position:absolute;inset:0;background:linear-gradient(100deg,#fbfaf8 0%,#f1ede6 45%,#e9e2d6 70%,#efe9df 100%)}
.left-fade{position:absolute;left:0;top:0;width:220px;height:340px;background:linear-gradient(90deg,rgba(255,255,255,.95),rgba(255,255,255,.6) 80%,rgba(255,255,255,0))}
.swoosh{position:absolute;inset:0;width:668px;height:518px}
.facts{position:absolute;left:16px;top:17px;width:210px;font-size:6.9px;line-height:1.5;color:#222}
.facts ul{list-style:none}
.facts li{position:relative;padding-left:6px}
.facts li::before{content:"•";position:absolute;left:0}
.facts .gap{margin-top:6px}
.tips{margin-top:10px;font-size:5.9px;line-height:1.5}
.tips ul{padding-left:3px}
.tips ul ul{padding-left:5px}
.brand{font-weight:600;letter-spacing:-.5px;line-height:1}
.brand .mark{display:inline-block;width:.35em;height:.35em;background:currentColor;margin-left:.12em;vertical-align:.55em}
.company-block{position:absolute;left:252px;top:150px;width:176px;text-align:center}
.company-block .brand{font-size:24px;color:var(--heading-grey)}
.company-block p{margin-top:8px;font-size:11.5px;line-height:1.4;color:#222}
.brand--white{position:absolute;left:48px;top:425px;font-size:24px;color:#fff}
.cover-title{position:absolute;left:448px;top:58px;width:210px;text-align:center}
.cover-title .brand{font-size:34px;color:var(--heading-grey)}
.cover-sub{margin-top:9px;font-size:13px;font-weight:600;color:var(--magenta)}
.rule-title{display:flex;align-items:center;gap:6px;margin-top:5px;font-size:11px;font-weight:700;color:#111}
.rule-title::before,.rule-title::after{content:"";flex:1;height:1px;background:var(--magenta)}
.mission-text{margin-top:3px;font-size:8.4px;line-height:1.45;color:#111}
.focus{position:absolute;left:456px;top:418px;width:197px}
.focus h3{display:flex;align-items:center;gap:4px;font-size:10px;font-weight:700;color:#fff}
.focus h3::before{content:"";flex:1;height:1px;background:#fff}
.focus p{margin-top:3px;font-size:6.6px;line-height:1.5;color:#fff;text-align:justify}

/* inside */
.photo{position:absolute;top:0;height:176px}
.photo--meeting{left:0;width:228px;background:linear-gradient(120deg,#5b6f86,#c9b8a6 55%,#8a3a3a)}
.photo--threshold{left:228px;width:146px;background:linear-gradient(180deg,#b07a3a,#8a5a28 55%,#3a3330 70%,#a58b72)}
.photo--grabbar{left:375px;top:0;width:69px;height:86px;background:linear-gradient(160deg,#5a5a5a,#9a9a9a)}
.photo--camera{left:375px;top:87px;width:69px;height:89px;background:linear-gradient(160deg,#9a7d58,#d8d2c8)}
.photo--filter{left:444px;width:224px;background:linear-gradient(120deg,#e8ecef,#f4f6f7 50%,#7fa6c9)}
.photo-label{position:absolute;color:#fff;font-size:7.5px}
.photo-label--small{font-size:4px}
.col{position:absolute;top:176px;height:340px}
.col--assess{left:0;width:228px;background:var(--paper);border-top:2px solid var(--blue-bar)}
.col--install{left:228px;width:216px;background:linear-gradient(180deg,#f7f7f7,#e4e4e4);border-top:2px solid var(--pink-bar)}
.col--plan{left:444px;width:224px;background:var(--blue-soft);border-top:2px solid var(--blue-bar)}
.col-bar{position:absolute;left:0;right:0;bottom:0;height:11px}
.col--assess .col-bar{background:var(--blue-bar)}
.col--install .col-bar{background:var(--pink-bar)}
.col--plan .col-bar{background:var(--grey-bar)}
.col h2{font-size:14px;line-height:1.4;font-weight:600}
.col p{font-size:7.6px;line-height:1.45}
.col--assess h2{position:absolute;left:20px;top:27px;color:var(--blue)}
.col--assess .body{position:absolute;left:20px;top:73px;width:192px}
.col--assess .cert{margin-top:10px;font-weight:700}
.tagline{margin-top:9px;font-size:13.5px;font-style:italic;color:#111}
.badge{position:absolute;left:48px;background:#d9e3f1}
.badge--one{top:206px;width:130px;height:40px;background:#e3e9f4}
.badge--two{top:258px;left:72px;width:80px;height:56px;border-radius:50%;background:#e2efe2}
.col--install h2{position:absolute;left:16px;top:27px;width:190px;color:var(--magenta)}
.checks{list-style:none;font-size:7.5px;line-height:1.46}
.checks li{position:relative;padding-left:11px}
.checks li::before{content:"";position:absolute;left:1px;top:2px;width:3px;height:5px;border-right:1.2px solid #555;border-bottom:1.2px solid #555;transform:rotate(40deg)}
.col--install .checks{position:absolute;left:16px;top:118px;width:195px}
.faint-brand{position:absolute;left:0;right:0;top:290px;text-align:center;font-size:19px;color:#cfcfcf}
.col--plan h2{position:absolute;left:15px;top:30px;color:#222}
.col--plan .body{position:absolute;left:15px;top:53px;width:196px}
.col--plan .body p + p{margin-top:10px}
.col--plan .checks{position:absolute;left:17px;top:162px;width:196px;line-height:1.5}
</style>
</head>
<body>

<section class="sheet sheet--outside">
  <div class="room-photo" role="img" aria-label="Bright, modern white living room with sofa and coffee table"></div>
  <div class="left-fade"></div>
  <svg class="swoosh" viewBox="0 0 834 647" preserveAspectRatio="none" aria-hidden="true">
    <path d="M0,340 C200,480 480,510 752,407 C600,505 350,600 0,612 Z" fill="#c2185b"/>
    <path d="M0,612 C350,600 600,505 752,407 C790,393 815,388 834,384 L834,647 L0,647 Z" fill="#58585a"/>
  </svg>

  <div class="facts">
    <ul>
      <li>Treating fall injuries is very costly.<br>In 2013, direct medical costs for falls—what patients and insurance companies pay—totaled $34 billion.... and it may reach $67.7 billion by 2020.</li>
      <li>Each year, 2.8 million people 65 and older are treated in emergency departments because of falls.</li>
      <li>Over 800,000 patients a year are hospitalized because of a fall injury, most often because of a broken hip or head injury.</li>
      <li>Each year at least 250,000 older people are hospitalized for hip fractures. More than 95% of hip fractures are caused by falling, usually by falling sideways.</li>
      <li class="gap">The average hospital cost for a fall injury is $35,000.</li>
      <li>The costs of treating fall injuries goes up with age.</li>
    </ul>
    <div class="tips">
      NHSA states four things you can do to prevent falls:
      <ul>
        <li>Begin an exercise program to improve your leg strength &amp; balance</li>
        <li>Ask your doctor or pharmacist to review your medicines</li>
        <li>Get annual eye check-ups &amp; update your eyeglasses</li>
        <li><strong>Make your home safer by:</strong>
          <ul>
            <li>Removing clutter &amp; tripping hazards</li>
            <li>Putting railings on all stairs &amp; adding grab bars in the bathroom</li>
            <li>Having good lighting, especially on stairs</li>
          </ul>
        </li>
      </ul>
    </div>
  </div>

  <div class="company-block">
    <div class="brand">NestWell<span class="mark"></span></div>
    <p>Company Information<br>goes here</p>
  </div>

  <div class="brand brand--white">NestWell<span class="mark"></span></div>

  <div class="cover-title">
    <div class="brand">NestWell<span class="mark"></span></div>
    <div class="cover-sub">NestWell Solutions</div>
    <h3 class="rule-title">Mission</h3>
    <p class="mission-text">To Improve the technology, ergonomics, safety, and maintenance of our client's homes to enhance their overall quality of life.</p>
  </div>

  <div class="focus">
    <h3>- Focus</h3>
    <p>We deliver light home modification service to seniors and boomers so their homes continue to meet their changing needs. Specifically, we provide consultation and aging in place assessments to homeowners, sales, and installation of high quality grab bars, threshold ramps, lighting, and smart home technology as well ongoing home maintenance through a home “Fitness Plan”.</p>
  </div>
</section>

<section class="sheet sheet--inside">
  <div class="photo photo--meeting" role="img" aria-label="Consultant reviewing paperwork with an older couple"></div>
  <div class="photo photo--threshold" role="img" aria-label="Rubber threshold ramp at a wooden doorway"><span class="photo-label" style="left:46px;top:162px">Accessibility</span></div>
  <div class="photo photo--grabbar" role="img" aria-label="Grab bar mounted on a tiled shower wall"><span class="photo-label photo-label--small" style="left:28px;top:78px">Safety</span></div>
  <div class="photo photo--camera" role="img" aria-label="Indoor security camera on a shelf"><span class="photo-label photo-label--small" style="left:24px;top:82px">Technology</span></div>
  <div class="photo photo--filter" role="img" aria-label="Technician on a ladder replacing a ceiling HVAC filter"></div>

  <div class="col col--assess">
    <h2>Home Assessments<br>and Consulting</h2>
    <div class="body">
      <p>Our NestWell Evaluations is a room by room assessment of your homes ergonomics, safety, and usability looking at everything from how much lighting is in your closet to how you exit your shower every day! We want to make your home work better for you now and in the future.</p>
      <p class="cert">We are GHB Certified Aging in Place Specialists.</p>
      <p class="tagline">Install it before you need it!</p>
    </div>
    <div class="badge badge--one" role="img" aria-label="Builders association membership badge"></div>
    <div class="badge badge--two" role="img" aria-label="Aging-in-place specialist certification badge"></div>
    <div class="col-bar"></div>
  </div>

  <div class="col col--install">
    <h2>We install and maintain a wide variety of products to make your home a NestWell!</h2>
    <ul class="checks">
      <li>Grab Bars, rails,</li>
      <li>Threshold Ramps</li>
      <li>Door Handles/Locks</li>
      <li>Motion sensor LED lighting</li>
      <li>Smoke/Carbon/Natural Gas Detectors</li>
      <li>Fire Extinguishers</li>
      <li>Rug Tape</li>
      <li>Bathtub and Bathroom traction mats/stickers</li>
      <li>TagTrack for keys and cell phone</li>
      <li>Front door cameras, indoor cameras</li>
      <li>Aura Speaker or HomeHub</li>
    </ul>
    <div class="faint-brand brand">NestWell</div>
    <div class="col-bar"></div>
  </div>

  <div class="col col--plan">
    <h2>Home Fitness Plan</h2>
    <div class="body">
      <p>Our NestWell Fitness Plans are perfect for every homeowner! Who can remember all the small tasks we are supposed to do as homeowners? Changing the filter in your HVAC or cleaning out the dryer venting? We take care of it so you don't have to remember.</p>
      <p>We provide periodic home maintenance to homeowner to keep their homes “Fit” including:</p>
    </div>
    <ul class="checks">
      <li>Maintain any and all NestWell installed products (see above)</li>
      <li>Replace/clean HVAC Filters</li>
      <li>Clean Dryer Vents</li>
      <li>Test Smoke Detectors, CO, NG detectors</li>
      <li>Replace light bulbs (60 W and 100 W white and soft white in stock, all others need to be provided by homeowner</li>
      <li>Replace Refrigerator Filters</li>
      <li>Check Garage Door chain</li>
    </ul>
    <div class="col-bar"></div>
  </div>
</section>

</body>
</html>
```